Medical VIP club - small design

Please read the specs in a design brief attached. Also we don't have logo in a Vector format and attaching the only version we have.

Industry/Entity Type

Club

```html
<!DOCTYPE html>
<html lang="en">
<head>
<meta charset="utf-8">
<title>Velmora — Packages and Prices</title>
<link href="https://fonts.googleapis.com/css2?family=Gelasio:ital,wght@0,400;0,600;0,700;1,400;1,600;1,700&display=swap" rel="stylesheet">
<style>
:root{
  --topbar:#2d2111;
  --topbar-edge:#3b2b14;
  --bg-center:#7f2f10;
  --bg-edge:#4e1a08;
  --cream:#f3e2bd;
  --gold-link:#e7cf98;
  --panel-top:#e9d7a4;
  --panel-bottom:#dccb93;
  --nav-line:#8c7344;
  --ink:#3e3220;
  --muted:#8a7a54;
  --table-top:#ecd99e;
  --table-bottom:#c3ae7c;
  --rule:#a8956a;
  --footer:#3d0b07;
  --footer-text:#a88f66;
}
*{margin:0;padding:0;box-sizing:border-box}
html,body{width:1200px;height:1096px;overflow:hidden}
body{font-family:"Gelasio",Georgia,serif;color:var(--ink);
  background:radial-gradient(ellipse 70% 60% at 50% 35%,var(--bg-center),var(--bg-edge));position:relative}
.abs{position:absolute}
.topbar{left:0;top:0;width:1200px;height:52px;background:linear-gradient(var(--topbar-edge),var(--topbar));}
.topbar a{position:absolute;top:20px;color:var(--gold-link);text-decoration:none;font-size:18px}
.topbar .reg{left:873px;font-style:italic;font-weight:700}
.topbar .sign{left:998px;font-style:italic;text-decoration:underline;font-size:17px;top:19px}
.brand{display:flex;align-items:center;gap:10px;font-size:40px;font-weight:600;color:#c9a877}
.brand .dot{width:18px;height:18px;border-radius:50%;background:#c9a877}
.brand.head{left:114px;top:80px}
.contact{left:937px;top:91px;height:56px;border-left:2px solid #c9a46a;padding-left:14px;color:var(--cream)}
.contact .title{font-size:20px;font-weight:700;line-height:24px}
.contact .phone{font-size:19px;line-height:24px}
.panel{left:112px;top:170px;width:966px;height:818px;border:1px solid #f0e2bc;
  background:linear-gradient(var(--panel-top),var(--panel-bottom));box-shadow:0 0 12px rgba(0,0,0,.35)}
.nav{left:0;top:0;width:964px;height:36px;border-bottom:3px solid var(--nav-line);font-size:16px}
.nav span{position:absolute;top:7px}
.nav .bold{font-weight:700}
.nav .sep{color:#6b5a3a}
.pkg-table{left:28px;top:66px;width:912px;height:380px;border:1px solid var(--rule);
  background:linear-gradient(var(--table-top),var(--table-bottom) 90%)}
.vrule{position:absolute;top:0;height:379px;border-left:1px solid var(--rule)}
.row{position:absolute;left:11px;width:870px;display:grid;grid-template-columns:251px 223px 212px 184px;
  align-items:center;border-bottom:1px dotted #6f5f3d}
.row > *{text-align:center}
.row .label{text-align:left;padding-left:27px;font-style:italic;font-size:18px;color:var(--muted)}
.row.head{top:0;height:42px}
.row.head .label{font-size:22px;font-weight:700}
.row.head .col{font-size:19px;font-style:italic;font-weight:700;color:var(--muted)}
.row.item{height:33.5px}
.tick{width:20px;height:20px;display:block;margin:0 auto;fill:#7b6a46}
.subtotal{position:absolute;left:0;top:330px;width:910px;height:49px;border-top:1px solid var(--rule);
  background:linear-gradient(#f1e2b2,#d6c38f);display:grid;grid-template-columns:262px 223px 212px 213px;align-items:center}
.subtotal span{font-style:italic;font-size:21px;text-align:center}
.subtotal .price{font-weight:700;text-align:left;padding-left:88px;font-size:20px}
.subtotal .price.p2{padding-left:64px}
.subtotal .price.p3{padding-left:33px}
.subtotal .label{text-align:left;padding-left:58px;font-size:22px}
.avail{left:652px;top:503px;display:flex;align-items:center;gap:10px;font-style:italic;font-size:17px}
.avail svg{width:22px;height:20px}
.book{left:794px;top:487px;width:146px;height:43px;border:1px solid #8f7c54;
  background:linear-gradient(#e8d7a5,#c4af7c);font-style:italic;font-weight:700;font-size:17px;
  display:flex;align-items:center;justify-content:center}
.follow{left:772px;top:786px;font-size:15px}
.social{top:778px;width:26px;height:26px;border-radius:3px;background:linear-gradient(#c8b790,#8e7d59)}
.footer{left:0;top:988px;width:1200px;height:108px;background:var(--footer);color:var(--footer-text);font-size:15px}
.footer .links{position:absolute;left:122px;top:45px}
.footer .links b{font-weight:700}
.footer .copy{position:absolute;left:678px;top:45px}
.brand.foot{left:956px;top:30px;font-size:28px;gap:7px}
.brand.foot .dot{width:13px;height:13px}
</style>
</head>
<body>
<svg width="0" height="0" class="abs">
  <symbol id="tick" viewBox="0 0 20 20"><path d="M2 11 L5 9 L8 14 C11 8 14 4 19 1 L19 2 C15 6 12 11 9 19 L7 19 Z"/></symbol>
</svg>

<header class="abs topbar">
  <a class="reg" href="#">Registration</a>
  <a class="sign" href="#">Sign In</a>
</header>

<div class="abs brand head"><span class="dot"></span>Velmora</div>

<div class="abs contact">
  <div class="title">Contact Us</div>
  <div class="phone">01480-552-317</div>
</div>

<main class="abs panel">
  <nav class="abs nav">
    <span style="left:29px">Home</span><span class="sep" style="left:100px">|</span>
    <span class="bold" style="left:128px">About Us</span><span class="sep" style="left:241px">|</span>
    <span style="left:272px">V.I.P Club</span><span class="sep" style="left:382px">|</span>
    <span style="left:434px">Services</span><span class="sep" style="left:535px">|</span>
    <span style="left:592px">Packages and Prices</span><span class="sep" style="left:774px">|</span>
    <span class="bold" style="left:813px">Registration</span>
  </nav>

  <section class="abs pkg-table">
    <div class="vrule" style="left:262px"></div>
    <div class="vrule" style="left:485px"></div>
    <div class="vrule" style="left:697px"></div>

    <div class="row head"><span class="label">Packages</span><span class="col">Package 1</span><span class="col">Package 2</span><span class="col">Package 3</span></div>
    <div class="row item" style="top:42px"><span class="label">Packages</span><span><svg class="tick"><use href="#tick"/></svg></span><span><svg class="tick"><use href="#tick"/></svg></span><span><svg class="tick"><use href="#tick"/></svg></span></div>
    <div class="row item" style="top:75.5px"><span class="label">Packages</span><span></span><span></span><span><svg class="tick"><use href="#tick"/></svg></span></div>
    <div class="row item" style="top:109px"><span class="label">Packages</span><span></span><span><svg class="tick"><use href="#tick"/></svg></span><span><svg class="tick"><use href="#tick"/></svg></span></div>
    <div class="row item" style="top:142.5px"><span class="label">Packages</span><span><svg class="tick"><use href="#tick"/></svg></span><span><svg class="tick"><use href="#tick"/></svg></span><span><svg class="tick"><use href="#tick"/></svg></span></div>
    <div class="row item" style="top:176px"><span class="label">Packages</span><span></span><span></span><span><svg class="tick"><use href="#tick"/></svg></span></div>
    <div class="row item" style="top:209.5px"><span class="label">Packages</span><span><svg class="tick"><use href="#tick"/></svg></span><span><svg class="tick"><use href="#tick"/></svg></span><span><svg class="tick"><use href="#tick"/></svg></span></div>
    <div class="row item" style="top:243px"><span class="label">Packages</span><span></span><span><svg class="tick"><use href="#tick"/></svg></span><span><svg class="tick"><use href="#tick"/></svg></span></div>
    <div class="row item" style="top:276.5px"><span class="label">Packages</span><span><svg class="tick"><use href="#tick"/></svg></span><span><svg class="tick"><use href="#tick"/></svg></span><span><svg class="tick"><use href="#tick"/></svg></span></div>

    <div class="subtotal"><span class="label">Sub Total</span><span class="price">$000</span><span class="price p2">$000</span><span class="price p3">$000</span></div>
  </section>

  <div class="abs avail">
    <svg viewBox="0 0 22 20"><rect x="1" y="1" width="20" height="18" rx="2" fill="#f4ecd6" stroke="#9a8a68"/><rect x="1" y="1" width="20" height="5" fill="#9a8a68"/><path d="M9 9 L14 12 L9 15 Z" fill="#9a8a68"/></svg>
    <span>Availability</span>
  </div>
  <div class="abs book">Book Now</div>

  <span class="abs follow">Follow us</span>
  <span class="abs social" style="left:862px"></span>
  <span class="abs social" style="left:893px"></span>
  <span class="abs social" style="left:923px"></span>
</main>

<footer class="abs footer">
  <div class="links">Home | Vip Club | Services | Packages and Prices | <b>Registration</b></div>
  <div class="copy">© All Rights Reserved 2011 Velmora</div>
  <div class="abs brand foot"><span class="dot"></span>Velmora</div>
</footer>
</body>
</html>
```